General Dental Office Business Card

I run a private general dental office in southern California, and would like a refresh/redesign of my business card. I focus on quality care rather than volume. The email address on the uploaded current card should be updated to: info@marbleshoredental.example. The current card's logo is a deboss, but I am open to other ideas. The logo can be refreshed, but it is something that's been with me since the beginning of the office, so I wouldn't want a drastic redesign.
Target Market(s)
Adults 18-99, whoever needs dental services
Industry/Entity Type
Healthcare/Dental
Contact Information for Business Card
Name, Address, Phone, email
Colors
Designer to choose colors to be used in the design.
Requirements
Must have
- Logo (Same as original one in the uploaded file), space on back for appointment time/date

```html
<!DOCTYPE html>
<html lang="en">
<head>
<meta charset="utf-8">
<title>Marble Shore Dental – Business Card</title>
<link rel="stylesheet" href="https://fonts.googleapis.com/css2?family=Montserrat:wght@400;500&display=swap">
<style>
  :root {
    --sky: #8ad4ec;
    --ink: #666a6d;
    --paper: #ffffff;
    --backdrop: #232323;
    --ghost: #eef2f2;
  }
  * { box-sizing: border-box; margin: 0; padding: 0; }
  html, body { width: 1200px; height: 780px; overflow: hidden; }
  body {
    background: var(--backdrop);
    font-family: "Montserrat", sans-serif;
    position: relative;
  }
  .card {
    position: absolute;
    top: 57px;
    width: 380px;
    height: 665px;
    background: var(--paper);
    overflow: hidden;
    box-shadow: 0 10px 30px rgba(0,0,0,.5);
  }
  .card--back { left: 190px; }
  .card--front { left: 630px; }

  /* back: appointment side */
  .appointment { position: absolute; top: 40px; left: 40px; right: 40px; }
  .appointment__field {
    border-top: 1px solid var(--ink);
    text-align: center;
    font-size: 14px;
    color: var(--ink);
    padding-top: 2px;
    margin-bottom: 44px;
  }
  .brand-mark {
    position: absolute;
    top: 230px; left: 0; right: 0;
    display: flex; flex-direction: column; align-items: center; gap: 14px;
  }
  .brand-mark__dot {
    width: 160px; height: 160px; border-radius: 50%;
    background: var(--sky);
  }
  .brand-mark__name { font-size: 16px; font-weight: 500; color: var(--sky); letter-spacing: .5px; }
  .shoreline { position: absolute; left: 0; bottom: 0; width: 380px; height: 230px; }
  .shoreline__name {
    position: absolute; left: 0; right: 0; bottom: 38px;
    text-align: center; color: var(--paper);
    font-size: 30px; font-weight: 500; letter-spacing: 1px;
  }

  /* front: contact side */
  .doctor { position: absolute; top: 34px; right: 30px; text-align: right; }
  .doctor__name { font-size: 21px; font-weight: 500; color: var(--sky); letter-spacing: .5px; }
  .doctor__title { font-size: 14px; font-weight: 500; color: var(--ink); letter-spacing: .5px; }
  .practice-name {
    position: absolute; top: 24px; left: 24px;
    writing-mode: vertical-rl;
    font-size: 44px; font-weight: 400; color: var(--sky);
    letter-spacing: 1px; line-height: 1;
  }
  .ghost-mark {
    position: absolute; top: 150px; left: 110px; width: 230px;
    display: flex; flex-direction: column; align-items: center; gap: 12px;
  }
  .ghost-mark__ring {
    width: 190px; height: 190px; border-radius: 50%;
    border: 10px solid var(--ghost);
  }
  .ghost-mark__name { font-size: 16px; font-weight: 500; color: var(--ghost); letter-spacing: .5px; }
  .contact {
    position: absolute; right: 26px; bottom: 40px;
    text-align: right; font-size: 13.5px; line-height: 1.45; color: var(--ink);
    font-style: normal;
  }
  .contact__address { color: var(--sky); }
  .contact__label { color: var(--sky); margin-right: 4px; }
</style>
</head>
<body>

<section class="card card--back" aria-label="Card back with appointment fields">
  <div class="appointment">
    <p class="appointment__field">Appointment Date</p>
    <p class="appointment__field">Time</p>
  </div>
  <div class="brand-mark">
    <span class="brand-mark__dot" aria-hidden="true"></span>
    <span class="brand-mark__name">Marble Shore Dental</span>
  </div>
  <svg class="shoreline" viewBox="0 0 380 230" aria-hidden="true">
    <path d="M0 150 C70 130 90 140 150 110 S270 60 380 30 L380 230 L0 230 Z" fill="var(--sky)"/>
    <g fill="none" stroke="var(--sky)" stroke-width="7">
      <path d="M0 134 C70 114 90 124 150 94 S270 44 380 14"/>
      <path d="M0 118 C70 98 90 108 150 78 S270 28 380 -2"/>
    </g>
  </svg>
  <p class="shoreline__name">Marble Shore Dental</p>
</section>

<section class="card card--front" aria-label="Card front with contact details">
  <div class="practice-name">Marble Shore Dental</div>
  <div class="doctor">
    <p class="doctor__name">Daniel R. Moreno DDS</p>
    <p class="doctor__title">General Dentistry</p>
  </div>
  <div class="ghost-mark" aria-hidden="true">
    <span class="ghost-mark__ring"></span>
    <span class="ghost-mark__name">Marble Shore Dental</span>
  </div>
  <address class="contact">
    <p class="contact__address">1850 Harbor View Road</p>
    <p class="contact__address">Seabrook, CA 92999</p>
    <p>555-014-7391</p>
    <p>marbleshoredental.example</p>
    <p><span class="contact__label">email:</span>info@marbleshoredental.example</p>
    <p><span class="contact__label">web:</span>www.marbleshoredental.example</p>
  </address>
</section>

</body>
</html>
```